Estate Agent/Real Estate valuation tool

We need a design for our our new estate agent valuation tool.

The tool allows users to book a valuation of their house/property with the estate agent, after they choose there property they can then complete their details and choose a booking time.

The mock up of the design we want is attached to this project.(Main Screen)

This also needs to be responsive so the design is easy to use on a mobile device.

Target Market(s)

estate agents

Industry/Entity Type

Real Estate Agent

Number of Pages Required

1 page

Requirements
Must have
• Section 2 and 3 greyed out when user is on step 1
• Section 1 and 3 greyed out when user is on step 2
• Section 1 and 2 greyed out when the user is on step 3
• *** Design must be shown for mobile/ipad and desktop
Nice to have
• Clean and Simple
Should not have
• Dark colours

```html
<!DOCTYPE html>
<html lang="en">
<head>
<meta charset="utf-8">
<title>Ridgeline Estates – Book a Valuation</title>
<link href="https://fonts.googleapis.com/css2?family=Lato:wght@400;700;900&display=swap" rel="stylesheet">
<style>
  :root {
    --page-bg: #3c3d3f;
    --header-band: rgba(62, 63, 66, 0.88);
    --panel-body: rgba(58, 59, 62, 0.86);
    --panel-head-top: #f1f1f1;
    --panel-head-bottom: #8d8e90;
    --head-text: #6e6f72;
    --head-text-dim: #8c8d90;
    --field: #ffffff;
    --label: #ffffff;
    --button-top: #e4e4e4;
    --button-bottom: #8e8f91;
    --slot-bg: #eeeeee;
    --slot-text: #7c7d80;
    --time-top: #b8b9bb;
    --time-bottom: #808184;
    --day-active: #7fd67c;
    --sky-top: #cfd6dd;
    --sky-mid: #e9eef2;
    --facade: #9aa0a6;
  }
  * { box-sizing: border-box; margin: 0; padding: 0; }
  html, body { width: 1200px; height: 821px; overflow: hidden; }
  body { font-family: 'Lato', sans-serif; background: var(--page-bg); position: relative; }

  .backdrop {
    position: absolute; inset: 0;
    background:
      linear-gradient(115deg, var(--facade) 0%, #b9bec3 22%, transparent 40%),
      linear-gradient(180deg, var(--sky-top) 0%, var(--sky-mid) 45%, #c5ccd3 100%);
  }

  .site-header {
    position: absolute; left: 0; top: 0; width: 1200px; height: 245px;
    background: var(--header-band);
    display: flex; flex-direction: column; align-items: center; justify-content: center;
    color: #fff;
  }
  .brand-name { font-size: 44px; font-weight: 700; letter-spacing: 6px; }
  .brand-tagline { margin-top: 12px; font-size: 13px; font-weight: 700; letter-spacing: 0.3px; }

  .step-panel {
    position: absolute; top: 383px; width: 351px; height: 426px;
    background: var(--panel-body);
    border-radius: 4px; overflow: hidden;
  }
  .step-panel.property { left: 32px; }
  .step-panel.details  { left: 422px; }
  .step-panel.booking  { left: 812px; }

  .panel-title {
    height: 47px;
    background: linear-gradient(180deg, var(--panel-head-top), var(--panel-head-bottom));
    color: var(--head-text);
    font-size: 17px; font-weight: 900; letter-spacing: 0.3px;
    text-align: center; line-height: 47px;
  }
  .booking .panel-title, .property .panel-title { color: var(--head-text-dim); }

  .field-label {
    position: absolute; left: 15px;
    color: var(--label); font-size: 16px; font-weight: 900;
  }
  .field {
    position: absolute; left: 15px; width: 332px; height: 40px;
    background: var(--field);
  }
  .search-button {
    position: absolute; left: 236px; top: 95px; width: 111px; height: 40px;
    background: linear-gradient(180deg, #bfc0c2, #9c9d9f);
    color: #f4f4f4; font-size: 16px; text-align: center; line-height: 40px;
  }

  .proceed {
    position: absolute; left: 98px; top: 373px; width: 165px; height: 52px;
    border-radius: 4px 4px 0 0;
    background: linear-gradient(180deg, var(--button-top), var(--button-bottom));
    color: #fff; font-size: 20px; font-weight: 900; letter-spacing: 0.5px;
    text-align: center; line-height: 52px;
  }
  .booking .proceed { font-weight: 400; }

  .day-tabs {
    position: absolute; left: 5px; top: 69px;
    display: flex; gap: 4px;
  }
  .day-tab {
    width: 45px; height: 42px; background: #fff;
    font-size: 5.5px; font-weight: 700; color: #333;
    display: flex; align-items: center; justify-content: center; text-align: center;
  }
  .day-tab.active { background: var(--day-active); }

  .slot {
    position: absolute; left: 14px; width: 334px; height: 40px;
    background: var(--slot-bg); display: flex;
  }
  .slot-date {
    flex: 1; padding-left: 16px; line-height: 40px;
    color: var(--slot-text); font-size: 17px;
  }
  .slot-time {
    width: 83px; line-height: 40px; text-align: center;
    background: linear-gradient(180deg, var(--time-top), var(--time-bottom));
    color: #fff; font-size: 19px; font-weight: 700;
  }
</style>
</head>
<body>
  <div class="backdrop" role="img" aria-label="Photograph looking up at a modern building facade against a pale sky"></div>

  <header class="site-header">
    <div class="brand-name">RIDGELINE ESTATES</div>
    <div class="brand-tagline">Real Estate acquisition and Rehabilitation</div>
  </header>

  <section class="step-panel property">
    <h2 class="panel-title">STEP 1 OF 3 - PROPERTY DETAILS</h2>
    <span class="field-label" style="top:78px">POSTCODE</span>
    <div class="field" style="top:95px"></div>
    <div class="search-button">SEARCH</div>
    <div class="field" style="top:149px"></div>
    <div class="field" style="top:203px"></div>
    <div class="field" style="top:258px"></div>
    <div class="proceed">PROCEED</div>
  </section>

  <section class="step-panel details">
    <h2 class="panel-title">STEP 1 OF 3 - YOUR DETAILS</h2>
    <span class="field-label" style="top:78px">YOUR NAME</span>
    <div class="field" style="top:95px"></div>
    <span class="field-label" style="top:160px">YOUR EMAIL</span>
    <div class="field" style="top:179px"></div>
    <span class="field-label" style="top:241px">YOUR CONTACT NUMBER</span>
    <div class="field" style="top:258px"></div>
    <div class="proceed">PROCEED</div>
  </section>

  <section class="step-panel booking">
    <h2 class="panel-title">STEP 1 OF 3 - PROPERTY DETAILS</h2>
    <div class="day-tabs">
      <div class="day-tab">TODAY</div>
      <div class="day-tab active">TOMORROW</div>
      <div class="day-tab">MON 30TH</div>
      <div class="day-tab">TUE 1ST</div>
      <div class="day-tab">WED 2ND</div>
      <div class="day-tab">THU 3RD</div>
      <div class="day-tab">FRI 4TH</div>
    </div>
    <div class="slot" style="top:125px"><span class="slot-date">SUNDAY 29TH NOVEMBER</span><span class="slot-time">08:30</span></div>
    <div class="slot" style="top:172px"><span class="slot-date">SUNDAY 29TH NOVEMBER</span><span class="slot-time">10:30</span></div>
    <div class="slot" style="top:219px"><span class="slot-date">SUNDAY 29TH NOVEMBER</span><span class="slot-time">12:30</span></div>
    <div class="slot" style="top:267px"><span class="slot-date">SUNDAY 29TH NOVEMBER</span><span class="slot-time">14:30</span></div>
    <div class="slot" style="top:312px"><span class="slot-date">SUNDAY 29TH NOVEMBER</span><span class="slot-time">16:30</span></div>
    <div class="proceed">PROCEED</div>
  </section>
</body>
</html>
```